OWNERS HANDBOOK

Take a MICROSOFT WORD document and turn it into a nicely designed and structured PDF or similar to circulate to Owners and to make available online for Owners to access.

```html
<!DOCTYPE html>
<html lang="en">
<head>
<meta charset="utf-8">
<title>Casa Luma Owners Handbook 2023-2024</title>
<link href="https://fonts.googleapis.com/css2?family=Archivo+Black&family=Arimo:wght@700&family=Playfair+Display:wght@700;900&display=swap" rel="stylesheet">
<style>
  :root {
    --backdrop: #d9d9d9;
    --paper: #ffffff;
    --ink: #2b2b2b;
    --ink-black: #111111;
    --navy: #36678a;
    --cyan: #00f5f7;
    --cream: #fdf3e3;
  }
  * { margin: 0; padding: 0; box-sizing: border-box; }
  html, body { width: 1200px; height: 1200px; overflow: hidden; background: var(--backdrop); }
  .canvas { position: relative; width: 1200px; height: 1200px; }

  .page { position: absolute; top: 200px; width: 523px; height: 741px; background: var(--paper); overflow: hidden; }
  .page--cover { left: 68px; }
  .page--preface { left: 607px; }

  /* Cover */
  .cover__photo { position: absolute; left: 0; top: 0; width: 523px; height: 530px;
    background: linear-gradient(180deg, #34578a 0%, #6f90bb 30%, #d8dbd6 44%, #c9c4b4 52%, #5f7f4a 60%, #5cb4d8 72%, #4a9fc8 80%, #e5e3dc 100%); }
  .cover__art { position: absolute; left: 0; top: 0; }
  .cover__kicker { position: absolute; left: 29px; top: 531px; font: 700 12.5px/1 "Playfair Display", serif; color: var(--ink); }
  .cover__title { position: absolute; left: 29px; top: 545px; font: 900 26px/1 "Playfair Display", serif; color: var(--ink); letter-spacing: 0.2px; }
  .cover__address { position: absolute; left: 29px; top: 591px; font: 700 14.5px/26px "Playfair Display", serif; color: var(--ink); }
  .cover__rule { position: absolute; left: 29px; top: 645px; width: 272px; height: 3px; background: var(--navy); }
  .cover__handbook { position: absolute; left: 30px; top: 657px; font: 900 25px/1 "Playfair Display", serif; color: var(--ink); }
  .cover__years { position: absolute; left: 30px; top: 686px; font: 700 25px/1 "Arimo", sans-serif; color: var(--ink); }
  .cover__social { position: absolute; left: 387px; top: 676px; display: flex; gap: 13px; }
  .cover__social span { width: 11px; height: 11px; border-radius: 50%; background: var(--navy); display: block; }
  .cover__date { position: absolute; left: 388px; top: 698px; font: 700 9px/1 "Playfair Display", serif; color: var(--ink); }

  /* Preface */
  .preface__art { position: absolute; left: 0; top: 0; }
  .preface__title { position: absolute; left: 27px; top: 313px; font: 900 32px/1 "Playfair Display", serif; color: var(--navy); }
  .preface__subtitle { position: absolute; left: 27px; top: 360px; font: 700 16px/1 "Playfair Display", serif; color: var(--navy); }
  .preface__body { position: absolute; left: 27px; width: 465px; font: 400 11.6px/17px "Archivo Black", sans-serif; color: var(--ink-black); text-align: justify; text-align-last: left; }
  .preface__body--one { top: 400px; }
  .preface__body--two { top: 486px; }
  .gallery__caption { position: absolute; top: 643px; width: 92px; font: 700 4.6px/1.15 "Playfair Display", serif; color: var(--ink-black); text-align: center; }
</style>
</head>
<body>
<div class="canvas">

  <section class="page page--cover">
    <div class="cover__photo" role="img" aria-label="Photograph of white resort apartment blocks with terracotta roofs behind a rectangular swimming pool and sun loungers under a blue sky"></div>
    <svg class="cover__art" width="523" height="741" viewBox="0 0 523 741" aria-hidden="true">
      <polygon fill="#ffffff" points="0,412 12,409 22,416 34,420 45,424 56,427 70,430 84,429 98,434 120,437 140,440 160,441 180,445 205,448 230,451 255,455 273,457 300,460 330,464 366,469 395,475 420,484 445,492 470,500 495,509 510,514 523,519 523,741 0,741"/>
      <polyline fill="none" stroke="#ffffff" stroke-width="1.4" points="53,509 53,45 471,45 471,509"/>
    </svg>
    <div class="cover__kicker">CASA LUMA VILLAGE AND</div>
    <div class="cover__title">ORCHARD GARDENS</div>
    <div class="cover__address">CASA LUMA RESORT, 4410 – 218,<br>PRAIA ALTA PORTUGAL</div>
    <div class="cover__rule"></div>
    <div class="cover__handbook">OWNERS HANDBOOK</div>
    <div class="cover__years">2023-2024</div>
    <div class="cover__social"><span></span><span></span><span></span><span></span></div>
    <div class="cover__date">4RTH MARCH, 2023</div>
  </section>

  <section class="page page--preface">
    <svg class="preface__art" width="523" height="741" viewBox="0 0 842 1192" aria-hidden="true">
      <defs>
        <linearGradient id="poolPhoto" x1="0" y1="0" x2="0" y2="1">
          <stop offset="0" stop-color="#2f7fd0"/>
          <stop offset="0.25" stop-color="#8fb6d8"/>
          <stop offset="0.38" stop-color="#d9b49a"/>
          <stop offset="0.5" stop-color="#5c8a3e"/>
          <stop offset="0.62" stop-color="#4fd3e0"/>
          <stop offset="1" stop-color="#27b4cf"/>
        </linearGradient>
      </defs>
      <path fill="var(--cyan)" d="M0,235 C90,180 210,185 320,240 C430,300 520,420 620,520 C700,600 780,620 842,630 V0 H0 Z"/>
      <path fill="var(--navy)" d="M0,195 C100,175 200,180 300,230 C410,290 470,380 560,440 C640,490 760,500 842,455 V0 H0 Z"/>
      <circle cx="600" cy="160" r="235" fill="var(--cream)"/>
      <circle cx="636" cy="170" r="215" fill="url(#poolPhoto)" role="img" aria-label="Photograph of a turquoise lagoon pool edged by palm trees and pink townhouses"/>
      <path fill="var(--navy)" d="M470,1192 C500,1135 560,1115 650,1105 C760,1093 805,1030 842,945 V1192 Z"/>
      <path fill="none" stroke="var(--navy)" stroke-width="1.4" d="M400,1192 C470,1140 540,1125 620,1115 C760,1098 790,1020 842,865"/>
      <g fill="none" stroke="var(--navy)" stroke-width="1.4">
        <circle cx="218" cy="960" r="67"/>
        <circle cx="416" cy="960" r="67"/>
        <circle cx="614" cy="960" r="67"/>
      </g>
      <circle cx="218" cy="962" r="60" fill="#6aa8c4" role="img" aria-label="Photograph of a pool framed by palm trees and a wicker chair"/>
      <circle cx="416" cy="962" r="60" fill="#4b9ac4" role="img" aria-label="Photograph of a resort pool with red flowering shrubs"/>
      <circle cx="614" cy="962" r="60" fill="#3f8fd0" role="img" aria-label="Photograph of a bright blue pool in front of apartment blocks"/>
    </svg>
    <h1 class="preface__title">PREFACE</h1>
    <h2 class="preface__subtitle">OWNERS HANDBOOK - 2023</h2>
    <p class="preface__body preface__body--one">THIS HANDBOOK HAS BEEN CONSTRUCTED AND PRODUCED FOR THE BENEFIT OF THE CASA LUMA OWNERS AND HAS BEEN PRODUCED BY EXISTING CASA LUMA OWNERS WHO HAVE VOLUNTEERED THEIR TIME AND EFFORTS IN THE HANDBOOK’S PRODUCTION.</p>
    <p class="preface__body preface__body--two">IF ANYTHING OF NOTE IS MISSING OR INCORRECT, THEN PLEASE LET A BOARD MEMBER KNOW AND THIS WILL ENSURE THE NEXT VERSION IS IMPROVED.</p>
    <p class="gallery__caption" style="left:89px">Shared pools and gardens stay open for owners and guests through every season of the year.</p>
    <p class="gallery__caption" style="left:212px">Quiet courtyards, shaded terraces and palm walks link every block of the resort together.</p>
    <p class="gallery__caption" style="left:335px">Pool hours, towel rules and upkeep dates are listed in the facilities chapter of this book.</p>
  </section>

</div>
</body>
</html>
```